Hops, Riffs & Sunset Grillout.

I need an A3 Poster, Insta Square and Facebook Event Cover photo for a Hops Riffs and Grill Event. Details as follows:

Name: Hops, Riffs and Sunset Grill
12pm - Late. Jan 26th at Copperleaf Yard Brewhouse
Acts:
Blue Tern - 7pm
Velvet Kite & Slow Morris - 3pm - 7pm
Grant Whitcombe - 12pm -3pm

Free BBQ 2-4pm.

```html
<!DOCTYPE html>
<html lang="en">
<head>
<meta charset="utf-8">
<title>Hops, Riffs and Sunset Grill – Event Set</title>
<link href="https://fonts.googleapis.com/css2?family=Montserrat:wght@500;600;700;800&family=Yellowtail&display=block" rel="stylesheet">
<style>
  :root{
    --backdrop:#e8e6e6;
    --teal:#45ae98;
    --ink:#111923;
    --white:#ffffff;
    --sun:#f8c652;
    --gold:#d9a93a;
    --art-a:#f8c652;
    --art-b:#e8493a;
    --sans:"Montserrat", Arial, sans-serif;
    --script:"Yellowtail", "Brush Script MT", cursive;
  }
  *{margin:0;padding:0;box-sizing:border-box}
  html,body{width:1200px;height:1200px;overflow:hidden;background:var(--backdrop)}
  .board{position:relative;width:1200px;height:1200px}
  .piece{position:absolute;overflow:hidden;background:var(--teal);box-shadow:0 6px 14px rgba(0,0,0,.28)}
  .piece .backdrop{position:absolute;inset:0;width:100%;height:100%}
  .c{position:absolute;left:50%;transform:translateX(-50%);white-space:nowrap;text-align:center}
  .brand{font-family:var(--sans);font-weight:800;color:var(--ink);line-height:1.05;letter-spacing:.04em;text-transform:uppercase}
  .title{font-family:var(--script);font-weight:400;color:var(--white);line-height:1.05;
    text-shadow:1px 1px 0 var(--ink),-1px -1px 0 var(--ink),1px -1px 0 var(--ink),-1px 1px 0 var(--ink),2px 2px 0 var(--ink)}
  .art{position:absolute;border-radius:40% 40% 46% 46%;background:linear-gradient(120deg,var(--art-a) 0%,var(--art-a) 42%,var(--art-b) 58%,var(--art-b) 100%)}
  .time{font-family:var(--sans);font-weight:700;color:var(--teal);display:flex;align-items:center;gap:.5em}
  .time::before,.time::after{content:"";display:block;width:2.6em;height:2px;background:var(--gold)}
  .date,.act{font-family:var(--sans);font-weight:500;color:var(--white)}
  .acts-label{font-family:var(--script);font-weight:400;color:var(--teal)}
  .bbq{font-family:var(--sans);font-weight:700;color:var(--ink);background:var(--sun);border-radius:2px;box-shadow:1px 1px 0 var(--teal);padding:0 .45em;line-height:1.45}

  /* A3 poster */
  .poster{left:477px;top:64px;width:246px;height:346px}
  .poster .brand{top:8px;font-size:8px}
  .poster .title{top:48px;font-size:27px}
  .poster .art{left:51px;top:112px;width:146px;height:112px}
  .poster .time{top:230px;font-size:12px}
  .poster .date{top:248px;font-size:7.5px}
  .poster .acts-label{top:262px;font-size:14px}
  .poster .act{font-size:8px}
  .poster .a1{top:283px}.poster .a2{top:296px}.poster .a3{top:309px}
  .poster .bbq{top:325px;font-size:8.5px}

  /* Facebook event cover */
  .cover{left:325px;top:471px;width:550px;height:288px}
  .cover .brand{position:absolute;left:13px;top:14px;font-size:15px;text-align:left}
  .cover .art{left:14px;top:90px;width:232px;height:182px}
  .cover .right{position:absolute;left:300px;top:0;width:250px;height:288px}
  .cover .title{top:14px;font-size:35px}
  .cover .time{top:116px;font-size:17px}
  .cover .date{top:140px;font-size:11px}
  .cover .acts-label{top:170px;font-size:21px}
  .cover .act{font-size:11.5px}
  .cover .a1{top:199px}.cover .a2{top:216px}.cover .a3{top:233px}
  .cover .bbq{top:256px;font-size:12px}

  /* Instagram square */
  .square{left:445px;top:818px;width:310px;height:309px}
  .square .brand{top:9px;font-size:8px}
  .square .title{top:40px;font-size:24px}
  .square .art{left:81px;top:75px;width:148px;height:113px}
  .square .time{top:197px;font-size:11px}
  .square .date{top:213px;font-size:7.5px}
  .square .acts-label{top:226px;font-size:13px}
  .square .act{font-size:7.5px}
  .square .a1{top:250px}.square .a2{top:262px}.square .a3{top:274px}
  .square .bbq{top:290px;font-size:8.5px}
</style>
</head>
<body>
<main class="board">

  <section class="piece poster" aria-label="A3 poster">
    <svg class="backdrop" viewBox="0 0 246 346" preserveAspectRatio="none"><path d="M0 200 Q60 238 140 222 Q200 208 246 181 L246 346 L0 346 Z" fill="var(--ink)"/></svg>
    <div class="brand c">Copperleaf Yard<br>Brewhouse</div>
    <h1 class="title c">Hops, Riffs and<br>Sunset Grill</h1>
    <div class="art" role="img" aria-label="Illustration of a frothy pint of beer beside a red kettle barbecue with flames"></div>
    <div class="time c">12pm - Late</div>
    <p class="date c">Jan 26th at Copperleaf Yard Brewhouse</p>
    <div class="acts-label c">Acts:</div>
    <p class="act a1 c">Grant Whitcombe - 12pm - 3pm</p>
    <p class="act a2 c">Velvet Kite &amp; Slow Morris - 3pm - 7pm</p>
    <p class="act a3 c">Blue Tern - 7pm</p>
    <div class="bbq c">Free BBQ 2-4pm</div>
  </section>

  <section class="piece cover" aria-label="Facebook event cover">
    <svg class="backdrop" viewBox="0 0 550 288" preserveAspectRatio="none"><path d="M253 0 C300 55 320 175 232 288 L550 288 L550 0 Z" fill="var(--ink)"/></svg>
    <div class="brand">Copperleaf Yard<br>Brewhouse</div>
    <div class="art" role="img" aria-label="Illustration of a frothy pint of beer beside a red kettle barbecue with flames"></div>
    <div class="right">
      <h1 class="title c">Hops, Riffs and<br>Sunset Grill</h1>
      <div class="time c">12pm - Late</div>
      <p class="date c">Jan 26th at Copperleaf Yard Brewhouse</p>
      <div class="acts-label c">Acts:</div>
      <p class="act a1 c">Grant Whitcombe - 12pm - 3pm</p>
      <p class="act a2 c">Velvet Kite &amp; Slow Morris - 3pm - 7pm</p>
      <p class="act a3 c">Blue Tern - 7pm</p>
      <div class="bbq c">Free BBQ 2-4pm</div>
    </div>
  </section>

  <section class="piece square" aria-label="Instagram square">
    <svg class="backdrop" viewBox="0 0 310 309" preserveAspectRatio="none"><path d="M0 165 Q80 198 170 186 Q250 172 310 135 L310 309 L0 309 Z" fill="var(--ink)"/></svg>
    <div class="brand c">Copperleaf Yard<br>Brewhouse</div>
    <h1 class="title c">Hops, Riffs and Sunset Grill</h1>
    <div class="art" role="img" aria-label="Illustration of a frothy pint of beer beside a red kettle barbecue with flames"></div>
    <div class="time c">12pm - Late</div>
    <p class="date c">Jan 26th at Copperleaf Yard Brewhouse</p>
    <div class="acts-label c">Acts:</div>
    <p class="act a1 c">Grant Whitcombe - 12pm - 3pm</p>
    <p class="act a2 c">Velvet Kite &amp; Slow Morris - 3pm - 7pm</p>
    <p class="act a3 c">Blue Tern - 7pm</p>
    <div class="bbq c">Free BBQ 2-4pm</div>
  </section>

</main>
</body>
</html>
```